Casas de Nueva Aurora Flyer

Make me a flyer postcard 5 x 7 horizontal, one sided. I want main title to be "Casas de Nueva Aurora". It needs to say “Familias que se forman en la fe y valores humanos, y trabajan para llevar a otras familias al encuentro con Cristo y la Virgen María.”  We are in 4 places, include this:
Reuniones Cada Domingo
Los Olmos, Falls Church: 11:15am - 301-555-0142
Monte Claro, Sterling: 9:30am - 571-555-0187
Hogar Valle Sereno, 9:45am - 703-555-0163
Puerta Dorada, Winchester: 2:30pm - 540-555-0129
Include the logo attached, and use the picture attached as the main image, you can select the people from the image only and delete background or keep background but make it fit in nicely to the postcard.

```html
<!DOCTYPE html>
<html lang="es">
<head>
<meta charset="utf-8">
<title>Casas de Nueva Aurora — Postal</title>
<link rel="stylesheet" href="https://fonts.googleapis.com/css2?family=Oswald:wght@600&family=Roboto+Condensed:ital,wght@0,700;1,400&family=Pinyon+Script&display=swap">
<style>
  :root {
    --page: #e0e0e0;
    --brown-deep: #2e1308;
    --brown: #3d1a0c;
    --brown-warm: #4a2412;
    --gold: #f9bf2c;
    --white: #ffffff;
    --rule: #8a6a5e;
  }
  * { margin: 0; padding: 0; box-sizing: border-box; }
  html, body { width: 949px; height: 1200px; overflow: hidden; background: var(--page); }
  .postcard {
    position: absolute; left: 107px; top: 85px; width: 736px; height: 1030px;
    background:
      radial-gradient(ellipse 60% 30% at 50% 28%, var(--brown-warm), transparent 70%),
      radial-gradient(ellipse 70% 25% at 40% 88%, #3f1c0e, transparent 70%),
      linear-gradient(180deg, var(--brown) 0%, var(--brown-deep) 100%);
    overflow: hidden;
    font-family: "Roboto Condensed", sans-serif;
    color: var(--white);
  }
  .emblem { position: absolute; left: 63px; top: 20px; width: 109px; height: 152px; }
  .stamp-box { position: absolute; left: 645px; top: 34px; width: 52px; height: 52px; border: 1.5px solid var(--white); }
  .address-line { position: absolute; left: 503px; width: 197px; height: 1px; background: var(--white); }
  .title {
    position: absolute; left: 0; right: 0; top: 180px; text-align: center;
    font-family: "Oswald", sans-serif; font-weight: 600; font-size: 70px; line-height: 1;
    color: var(--gold); text-transform: uppercase; letter-spacing: -0.5px;
  }
  .mission {
    position: absolute; left: 20px; right: 20px; top: 267px; text-align: center;
    font-style: italic; font-size: 31px; line-height: 42px;
  }
  .group-photo {
    position: absolute; left: 0; top: 412px; width: 736px; height: 275px;
    border-top: 3px solid var(--gold);
    border-radius: 42px 42px 42px 42px;
    background: linear-gradient(180deg, #b9cfe0 0%, #4f7a3a 30%, #3b4a6a 60%, #8b6e88 85%, #d8c2b4 100%);
  }
  .meetings-rule { position: absolute; top: 743px; height: 1.5px; background: var(--gold); }
  .meetings-heading {
    position: absolute; left: 0; right: 0; top: 700px; text-align: center;
    font-family: "Pinyon Script", cursive; font-size: 62px; line-height: 1;
  }
  .locations {
    position: absolute; left: 33px; top: 785px; width: 670px; height: 213px;
    border: 1.5px dotted var(--white); display: flex;
  }
  .location { text-align: center; padding-top: 34px; }
  .location + .location { border-left: 1.5px dotted var(--white); }
  .location-name { font-style: italic; font-size: 22px; line-height: 27px; }
  .location-city { font-style: italic; font-size: 22px; line-height: 27px; color: var(--gold); }
  .location-divider { width: 90px; height: 1px; background: var(--rule); margin: 18px auto 20px; }
  .location-time { font-weight: 700; font-size: 20px; line-height: 28px; color: var(--gold); }
  .location-phone { font-weight: 700; font-size: 20px; line-height: 28px; }
</style>
</head>
<body>
  <main class="postcard">
    <svg class="emblem" viewBox="0 0 109 152" role="img" aria-label="Icono de la Sagrada Familia en marco dorado">
      <path d="M2 30 L54.5 2 L107 30 V150 H2 Z" fill="#a8823a" stroke="#e2b347" stroke-width="2"/>
      <path d="M10 34 L54.5 10 L99 34 V142 H10 Z" fill="#a8322a"/>
    </svg>

    <div class="stamp-box"></div>
    <div class="address-line" style="top:106px"></div>
    <div class="address-line" style="top:128px"></div>
    <div class="address-line" style="top:152px"></div>

    <h1 class="title">Casas de Nueva Aurora</h1>
    <p class="mission">Familias que se forman en la fe y valores humanos,<br>y trabajan para llevar a otras familias al encuentro<br>con Cristo y la Virgen María.</p>

    <div class="group-photo" role="img" aria-label="Foto grupal de las familias en un parque al aire libre"></div>

    <div class="meetings-rule" style="left:0;width:148px"></div>
    <div class="meetings-rule" style="left:598px;width:138px"></div>
    <h2 class="meetings-heading">Reuniones Cada Domingo</h2>

    <section class="locations">
      <div class="location" style="width:151px">
        <p class="location-name">Los Olmos,</p>
        <p class="location-city">Falls Church</p>
        <div class="location-divider"></div>
        <p class="location-time">11:15 am -</p>
        <p class="location-phone">301-555-0142</p>
      </div>
      <div class="location" style="width:168px">
        <p class="location-name">Monte Claro,</p>
        <p class="location-city">Sterling</p>
        <div class="location-divider"></div>
        <p class="location-time">9:30 am -</p>
        <p class="location-phone">571-555-0187</p>
      </div>
      <div class="location" style="width:174px">
        <p class="location-name">Hogar Valle</p>
        <p class="location-city">Sereno</p>
        <div class="location-divider"></div>
        <p class="location-time">9:45 am -</p>
        <p class="location-phone">703-555-0163</p>
      </div>
      <div class="location" style="flex:1">
        <p class="location-name">Puerta Dorada,</p>
        <p class="location-city">Winchester</p>
        <div class="location-divider"></div>
        <p class="location-time">2:30 pm -</p>
        <p class="location-phone">540-555-0129</p>
      </div>
    </section>
  </main>
</body>
</html>
```